Web Site Design For Real Estate Sales Project

The idea behind this project is pretty simple. I am putting my penthouse apartment up for sale and am trying to be creative in selling it.
Technically this will be pretty simple, it will be 3 pages but graphically this has to be as impressive as possible which is why I am trying Pixel Harbor.
The apartment is located in Barra Da Tijuca, Rio De Janeiro, Brazil. (This is where the 2016 Meridian Regatta will be held)
I am looking for an index page and 2 sub-pages. I am open to all kinds of designs and navigation's but it has to make an impression quickly with a professional and enticing design. The index page should make it obvious that there is a penthouse apartment for sale in Barra Da Tijuca ( suburb of Rio De Janeiro). The first sub page is about the Condominium where the apartment is located, the second sub page is about the apartment itself.
Here is a more detailed description of what the 3 pages should be about.
Index Page
This is the landing page and should make it obvious that there is an apartment for sale in Barra Da Tijuca, Rio De Janeiro with the following attributes
251 SQ M
Duplex Penthouse
4 suites
Price R$ 2.200.000
Price per SQ M: R$ 8.764
First Sub-Page
This is about the Condominium which is called "Gentle Palm Residences" with the following bullets
*Family friendly and safe
*Direct access to the beach
*Many amenities like pool, football court, gym, sauna
There should be some photos of the condominium and a link to the site of the condominium ( www.gprvx.com )
Second Sub-page
This is about the apartment. It should list in bullets the features of the apartment and then have a photo gallery of the view and various rooms. I have attached sample photos but will eventually have to use more photos.
Apartment Features
Price: R$ 2.220.000
251 m2 Duplex Penthouse
4 suites
maids room with bath
guest bathroom
living room
dinning room
Terrace with heated pool for year round use
Veranda
As mentioned above I am open to all designs and navigation so feel free to be creative. The important thing is catch peoples attention and get the message across in a few seconds, which is that there is an apartment for sale at this price with these features in this location. I will then use brightlist promoter and SEO to get people to the site.
Thanks
Target Market(s)
Men and Women from 30-60 years of age.
Industry/Entity Type
Apartment

```html
<!DOCTYPE html>
<html lang="en">
<head>
<meta charset="utf-8">
<title>Gentle Palm Residences – The Condominium</title>
<link rel="stylesheet" href="https://fonts.googleapis.com/css2?family=Federo&family=Josefin+Slab:wght@300;400&family=Oswald:wght@300;700&display=swap">
<style>
  :root {
    --page-dark: #1f1f1f;
    --panel-left: rgba(205, 205, 205, 0.62);
    --panel-right: rgba(228, 228, 228, 0.86);
    --panel-contact: #c9c9c9;
    --ink: #2b2b2b;
    --ink-soft: #444;
    --link: #1d6fc4;
    --btn-home: #3f6a8e;
    --btn-penthouse: #4d8db6;
    --rule: #4a4a4a;
  }
  * { box-sizing: border-box; margin: 0; padding: 0; }
  html, body { width: 1200px; height: 1010px; overflow: hidden; background: var(--page-dark); }
  .canvas { position: relative; width: 1200px; height: 1010px; background: var(--page-dark); overflow: hidden; }

  .hero-photo {
    position: absolute; left: 0; top: 28px; width: 1200px; height: 641px;
    background:
      radial-gradient(ellipse 40% 30% at 52% 18%, #8fc3cf 0%, rgba(143,195,207,0) 100%),
      radial-gradient(ellipse 25% 25% at 8% 55%, #79b3b2 0%, rgba(121,179,178,0) 100%),
      linear-gradient(160deg, #c9b98b 0%, #a89a68 40%, #8a7f54 70%, #6b6a3e 100%);
  }

  .gallery-photo { position: absolute; top: 689px; height: 221px; }
  .gallery-photo.terrace { left: 0; width: 393px; background: linear-gradient(180deg, #eef0ee 0%, #c9ccc8 50%, #8e8c85 100%); }
  .gallery-photo.driveway { left: 403px; width: 394px; background: linear-gradient(180deg, #a9c6e6 0%, #b59c86 40%, #7c7b74 100%); }
  .gallery-photo.gate { left: 807px; width: 393px; background: linear-gradient(180deg, #dcdcdc 0%, #9fa28c 45%, #a08a72 100%); }

  .condo-panel {
    position: absolute; left: 50px; top: 0; width: 506px; height: 349px;
    background: var(--panel-left); padding: 48px 0 0 12px;
  }
  .condo-title { font-family: "Federo", sans-serif; font-size: 41px; color: var(--ink); line-height: 1; letter-spacing: 0.3px; }
  .condo-points { list-style: none; margin: 24px 0 0 48px; font-family: "Oswald", sans-serif; font-weight: 300; font-size: 30px; color: var(--ink); line-height: 1.12; }
  .condo-points li { position: relative; margin-bottom: 14px; }
  .condo-points li::before { content: ""; position: absolute; left: -19px; top: 21px; width: 11px; height: 11px; border-radius: 50%; background: var(--ink); }
  .condo-points b { font-weight: 700; }

  .info-panel {
    position: absolute; left: 732px; top: 0; width: 443px; height: 437px;
    background: var(--panel-right); text-align: center;
  }
  .nav-button {
    position: absolute; top: 33px; width: 118px; height: 118px; border-radius: 50%;
    display: flex; align-items: center; justify-content: center; flex-direction: column;
    font-family: "Oswald", sans-serif; font-weight: 700; color: #fff; font-size: 27px; line-height: 1.05;
    text-decoration: none; box-shadow: 2px 4px 6px rgba(0,0,0,0.35);
  }
  .nav-button.home { left: 67px; background: var(--btn-home); }
  .nav-button.penthouse { left: 258px; background: var(--btn-penthouse); }
  .nav-rule { position: absolute; left: 0; top: 159px; }
  .info-text { position: absolute; left: 0; top: 180px; width: 443px; }
  .info-lead { font-family: "Josefin Slab", serif; font-size: 22px; color: var(--ink-soft); }
  .info-name { font-family: "Federo", sans-serif; font-size: 30px; color: var(--ink); margin-top: 4px; }
  .info-sub { font-family: "Josefin Slab", serif; font-size: 22px; color: var(--ink-soft); margin-top: 2px; }
  .info-list { list-style: none; margin-top: 14px; font-family: "Oswald", sans-serif; font-weight: 300; font-size: 19px; color: var(--ink); line-height: 1.75; }
  .info-list b { font-weight: 700; }
  .info-more { font-family: "Josefin Slab", serif; font-size: 25px; color: var(--ink); margin-top: 4px; }
  .info-more a { color: var(--link); text-decoration: none; }

  .contact-area {
    position: absolute; left: 50px; top: 885px; width: 505px; height: 125px;
    background: var(--panel-contact); display: flex; justify-content: center; padding-top: 38px;
    font-family: "Federo", sans-serif; font-size: 44px; color: var(--ink); letter-spacing: 0.5px;
  }
</style>
</head>
<body>
<div class="canvas">
  <div class="hero-photo" role="img" aria-label="Condominium pool deck seen from above with tables, umbrellas and sun loungers"></div>

  <section class="condo-panel">
    <h1 class="condo-title">Gentle Palm Residences</h1>
    <ul class="condo-points">
      <li>family <b>friendly</b> and <b>safe</b></li>
      <li><b>direct access</b> to the beach</li>
      <li>many amenities such as <b>pool</b>,<br><b>football court</b>, <b>gym</b>, <b>sauna</b></li>
    </ul>
  </section>

  <aside class="info-panel">
    <a class="nav-button home" href="#">HOMEPAGE</a>
    <a class="nav-button penthouse" href="#"><span>THE</span><span>PENTHOUSE</span></a>
    <svg class="nav-rule" width="443" height="10" viewBox="0 0 443 10" aria-hidden="true">
      <line x1="0" y1="5" x2="443" y2="5" stroke="var(--rule)" stroke-width="2"/>
      <circle cx="222" cy="5" r="5" fill="var(--rule)"/>
    </svg>
    <div class="info-text">
      <p class="info-lead">Familiar and comfortable condominium</p>
      <p class="info-name">Gentle Palm Residences</p>
      <p class="info-sub">has great recreational areas such as:</p>
      <ul class="info-list">
        <li>playground with <b>synthetic grass</b></li>
        <li><b>cinema</b> room and <b>restaurant</b></li>
        <li><b>sauna</b> and block-poly sports</li>
      </ul>
      <p class="info-more">You can find more info <a href="#">here</a></p>
    </div>
  </aside>

  <div class="gallery-photo terrace" role="img" aria-label="Shaded terrace with umbrellas, tables and chairs"></div>
  <div class="gallery-photo driveway" role="img" aria-label="Condominium entrance driveway with towers behind"></div>
  <div class="gallery-photo gate" role="img" aria-label="Condominium entrance gate with gardens"></div>

  <div class="contact-area">CONTACT AREA</div>
</div>
</body>
</html>
```